Business Card Design for Madam Rosette's Soak Parlor

Name: Madam Rosette's Soak Parlor. Maker of bath bombs, bath salts.

Card details:

Dolores Vantick
1.702.555.0193
Las Vegas Nevada
dvantick47@mailbrook.test

"Bath bombs, bath salts and more..."

Industry/Entity Type

Business

Contact Information for Business Card

A picture of an old-fashioned bathtub (with claw feet) filled with bath bombs.

Colors include: Lavender, Pink, Turquois, Light Blue. Can you make the overall design look old fashioned.

```html
<!DOCTYPE html>
<html lang="en">
<head>
<meta charset="utf-8">
<title>Madam Rosette's Soak Parlor — Business Card</title>
<link rel="stylesheet" href="https://fonts.googleapis.com/css2?family=Roboto:wght@400;700&display=swap">
<style>
  :root {
    --backdrop: #ecdcb8;
    --card: #111113;
    --accent-red: #e3202b;
    --text-white: #ffffff;
    --mark-grey: #e4e4e4;
  }
  * { margin: 0; padding: 0; box-sizing: border-box; }
  html, body {
    width: 1200px;
    height: 900px;
    overflow: hidden;
    background: var(--backdrop);
    font-family: "Roboto", Arial, sans-serif;
  }
  .business-card {
    position: absolute;
    left: 100px;
    top: 164px;
    width: 1000px;
    height: 573px;
    background: var(--card);
  }
  .brand-block {
    position: absolute;
    left: 414px;
    top: 84px;
    width: 540px;
    text-align: center;
  }
  .brand-dot {
    display: block;
    width: 64px;
    height: 64px;
    margin: 0 auto 34px;
    border-radius: 50%;
    background: var(--mark-grey);
  }
  .brand-name {
    color: var(--accent-red);
    font-weight: 700;
    font-size: 37px;
    line-height: 1;
    white-space: nowrap;
  }
  .brand-tagline {
    margin-top: 14px;
    color: var(--text-white);
    font-weight: 700;
    font-size: 26px;
    line-height: 1;
    white-space: nowrap;
  }
  .holder-name {
    position: absolute;
    left: 54px;
    top: 412px;
    color: var(--accent-red);
    font-weight: 700;
    font-size: 42px;
    line-height: 1;
    white-space: nowrap;
  }
  .divider {
    position: absolute;
    left: 425px;
    top: 415px;
    width: 4px;
    height: 133px;
    background: var(--accent-red);
  }
  .contact-list {
    position: absolute;
    left: 512px;
    top: 408px;
    list-style: none;
  }
  .contact-item {
    display: flex;
    align-items: center;
    height: 42px;
    font-size: 30px;
    color: var(--text-white);
    white-space: nowrap;
  }
  .contact-item--location { color: var(--accent-red); }
  .contact-icon {
    width: 22px;
    height: 22px;
    margin-right: 12px;
    flex: none;
  }
</style>
</head>
<body>
  <main class="business-card">
    <section class="brand-block">
      <span class="brand-dot" aria-hidden="true"></span>
      <h1 class="brand-name">Madam Rosette's Soak Parlor</h1>
      <p class="brand-tagline">"Bath bombs, bath salts and more...</p>
    </section>

    <h2 class="holder-name">Dolores Vantick</h2>
    <div class="divider" aria-hidden="true"></div>

    <ul class="contact-list">
      <li class="contact-item">
        <svg class="contact-icon" viewBox="0 0 24 24" aria-hidden="true">
          <path fill="#ffffff" d="M6.6 10.8c1.4 2.8 3.8 5.1 6.6 6.6l2.2-2.2c.3-.3.7-.4 1-.2 1.1.4 2.3.6 3.6.6.6 0 1 .4 1 1V20c0 .6-.4 1-1 1C10.6 21 3 13.4 3 4c0-.6.4-1 1-1h3.5c.6 0 1 .4 1 1 0 1.3.2 2.5.6 3.6.1.3 0 .7-.2 1z"/>
        </svg>
        1.702.555.0193
      </li>
      <li class="contact-item contact-item--location">
        <svg class="contact-icon" viewBox="0 0 24 24" aria-hidden="true">
          <path fill="#e3202b" d="M12 2C8.1 2 5 5.1 5 9c0 5.2 7 13 7 13s7-7.8 7-13c0-3.9-3.1-7-7-7zm0 9.5a2.5 2.5 0 1 1 0-5 2.5 2.5 0 0 1 0 5z"/>
        </svg>
        Las Vegas Nevada
      </li>
      <li class="contact-item">
        <svg class="contact-icon" viewBox="0 0 24 24" aria-hidden="true">
          <rect x="2" y="5" width="20" height="14" rx="1.5" fill="#ffffff"/>
        </svg>
        dvantick47@mailbrook.test
      </li>
    </ul>
  </main>
</body>
</html>
```